WordPress Blog/Website for Athlete Focused Sports Marketing Agency

WordPress Website that Serves two primary purposes:

1) Company Information Website which showcases organization's capabilities and work

2) Highlights, Showcases and Displays key information for athlete clients, aggregates all of the content they are creating(mostly social) and is a key portal for publishing press releases, news updates and more.

Key Criteria for Success:

Easily Updatable
Easy to Navigate
Clean Design that follows the function/form of the organization's brand identity while also incorporating the identity of the athletes.

Supporting Documentation:**These files are also uploaded and attached to this project description**
Creative Brief: https://files.vorteldrive.net/a/lumbrecrest.com/file/d/7Kx2PqRmWtZ4nJvLbHsYcEgAoUi/edit?usp=sharing
Logo Files/Designs are attached. Color Palette can be adjusted as necessary.

WireFrame: (Please use your own judgement and creative liberty's to make something that is a lot better then what I came up with):
https://files.vorteldrive.net/file/d/7Kx2PqRmWtZ4mBcNdFgHjKlQwEr/edit?usp=sharing

Current Website(Incomplete): www.lumbrecrest.com

Thanks!

Industry/Entity Type

It Company

Requirements
Must have
• Social Media Integration: A social feed that aggregates content across all channels for multiple users(all of my athletes)

"News=Blog" Portal that serves as the primary engine for the page's content

Professional Look and Design- it should look like a website, not a blog.

```html
<!DOCTYPE html>
<html lang="en">
<head>
<meta charset="utf-8">
<title>Lumbre &amp; Crest — Lifestyle &amp; Sports Marketing</title>
<link href="https://fonts.googleapis.com/css2?family=Rokkitt:wght@400&family=Ubuntu:wght@400;500&family=Arimo:wght@400;700&display=swap" rel="stylesheet">
<style>
:root{
  --orange:#e8730f;
  --orange-dark:#c95a06;
  --ink:#222;
  --text:#333;
  --footer:#3c3c3c;
  --band:#d97b2a;
  --white:#fff;
}
*{box-sizing:border-box;margin:0;padding:0}
html,body{width:799px;height:1200px;overflow:hidden}
body{position:relative;background:linear-gradient(90deg,#dcdcdc,#f7f7f7 20%,#f7f7f7 80%,#dcdcdc);font-family:Arimo,Arial,sans-serif;color:var(--text)}
.abs{position:absolute}
.navbar{left:0;top:26px;width:799px;height:30px;background:#050505}
.logo{left:74px;top:13px;width:213px;height:60px;background:var(--white);border:1px solid #ddd;box-shadow:0 2px 6px rgba(0,0,0,.2);display:flex;align-items:center;justify-content:center;font-family:Rokkitt,serif;font-size:28px;line-height:1;white-space:nowrap;overflow:hidden;color:var(--orange)}
.nav a{position:absolute;top:37px;color:#fff;font-size:9.5px;text-decoration:none;transform:translateX(-50%);white-space:nowrap}
.nav .home{left:378px;top:22px;width:40px;height:36px;background:var(--orange);transform:none;display:flex;align-items:center;justify-content:center;font-size:10px}
.social-top span{position:absolute;top:67px;width:16px;height:16px;border-radius:50%;background:#8a8a8a}
.slider{left:70px;top:92px;width:659px;height:298px;background:#fff;box-shadow:0 2px 8px rgba(0,0,0,.25)}
.slide-img{left:76px;top:97px;width:647px;height:288px;background:linear-gradient(180deg,#1b6e9e 0%,#2ea3cf 45%,#7e8f9b 70%,#a8563f 100%)}
.arrow{top:227px;width:32px;height:35px;background:#3a3a3a;color:#bbb;font-size:22px;display:flex;align-items:center;justify-content:center}
.caption{left:118px;top:242px;width:244px;height:128px;background:rgba(25,25,25,.82);padding:6px 10px}
.caption h2{font-family:Rokkitt,serif;font-weight:400;font-size:26px;color:var(--orange);line-height:30px;white-space:nowrap}
.caption p{font-size:6.6px;line-height:12px;color:#fff;font-weight:700;margin-top:8px}
.btn{background:linear-gradient(#f08a2a,var(--orange-dark));color:#fff;font-size:7px;border-radius:18px 18px 0 0;display:flex;align-items:center;justify-content:center;white-space:nowrap}
.title{font-family:Ubuntu,sans-serif;font-size:20px;color:var(--orange);width:799px;text-align:center;left:0;top:412px}
.title b{color:#444;font-weight:400}
.lead{left:78px;top:446px;width:634px;text-align:center;font-size:7.7px;line-height:12px;color:#222}
.divider{height:2px;background:radial-gradient(ellipse at center,#c8c8c8 0%,rgba(200,200,200,0) 70%)}
.col h3{position:absolute;font-family:Ubuntu,sans-serif;font-weight:400;font-size:14px;color:var(--orange);white-space:nowrap;transform:translateX(-50%)}
.frame{background:#fff;border:1px solid #ddd;padding:5px}
.frame div{width:100%;height:100%}
.col p{position:absolute;width:195px;font-size:7.9px;line-height:12px;text-align:justify;color:#333}
.vline{border-left:1px dashed #bbb;width:0}
.panel{left:70px;top:820px;width:644px;height:191px;background:#f2f2f2;border:2px solid #fff;border-radius:12px;box-shadow:0 0 6px rgba(0,0,0,.12)}
.panel h4{position:absolute;font-family:Ubuntu,sans-serif;font-weight:400;font-size:16px;color:#444}
.quote{position:absolute;left:92px;width:315px;font-size:7.4px;line-height:12px;color:#333}
.qmark{position:absolute;font-family:Georgia,serif;font-size:16px;color:#666}
.author{position:absolute;font-size:7px;color:var(--orange);white-space:nowrap}
.client{position:absolute;font-family:Arimo,sans-serif;font-weight:700;font-size:10px;color:#555;transform:translateX(-50%);display:flex;align-items:center;gap:3px;white-space:nowrap}
.client i{display:inline-block;width:8px;height:8px;border-radius:50%;background:#999}
.footer{left:0;top:1038px;width:799px;height:122px;background:var(--footer);border-top:2px solid #888}
.links li{position:absolute;left:84px;list-style:none;font-size:9px;color:#ddd;display:flex;align-items:center;gap:5px}
.nl-title{left:273px;top:1050px;font-family:Ubuntu,sans-serif;font-size:15px;color:#888;white-space:nowrap}
.nl-title b{color:#fff;font-weight:500}
.nl-text{left:274px;top:1082px;width:230px;font-size:7.4px;line-height:12px;color:#888}
.signup{left:274px;top:1114px;width:231px;height:32px;background:#1c1c1c;border-radius:3px}
.field{left:279px;top:1119px;width:168px;height:22px;background:#fff;font-size:7.2px;color:#222;padding:7px 6px}
.go{left:451px;top:1121px;font-size:7.4px;color:#fff;font-weight:700;width:50px;text-align:center;padding-top:6px}
.news-title{left:578px;top:1050px;font-family:Ubuntu,sans-serif;font-size:16px;color:#fff;white-space:nowrap}
.date{left:578px;width:26px;height:26px;background:#2a2a2a;border:1px solid #555;font-size:7px;color:#ddd;text-align:center;line-height:8px;padding-top:5px}
.news{left:614px;font-size:7.6px;line-height:11px;color:#aaa;width:130px}
.band{left:0;top:1160px;width:799px;height:40px;background:var(--band)}
.copy{left:76px;top:1175px;font-size:7.6px;color:#fff;white-space:nowrap}
.social-foot span{position:absolute;top:1166px;width:24px;height:24px;border-radius:50%;background:#f4f4f4}
</style>
</head>
<body>
<div class="abs navbar"></div>
<div class="abs logo">Lumbre &amp; Crest</div>
<nav class="nav">
  <a class="home" href="#">Home</a>
  <a href="#" style="left:468px">What We Do</a>
  <a href="#" style="left:550px">Athletes</a>
  <a href="#" style="left:623px">Gallery</a>
  <a href="#" style="left:705px">Contact Us</a>
</nav>
<div class="social-top" aria-label="Social links"><span style="left:635px"></span><span style="left:658px"></span><span style="left:681px"></span><span style="left:704px"></span></div>

<div class="abs slider"></div>
<div class="abs slide-img" role="img" aria-label="Sprinter crouched in starting blocks on a stadium track under floodlights"></div>
<div class="abs arrow" style="left:59px">‹</div>
<div class="abs arrow" style="left:709px">›</div>
<div class="abs caption">
  <h2>Lumbre &amp; Crest</h2>
  <p>Lorem Ipsum is simply dummy text of the printing and typesetting industry. Lorem Ipsum has been the industry's standard dummy text ever since the 1500s, when an unknown printer took a galley of type and scrambled it to make a type specimen book. It has survived not only five centuries, but also the leap into</p>
</div>
<div class="abs btn" style="left:309px;top:352px;width:46px;height:18px">Read More</div>

<div class="abs title">Lifestyle &amp; Sports <b>Marketing</b></div>
<p class="abs lead">Lorem Ipsum is simply dummy text of the printing and typesetting industry. Lorem Ipsum has been the industry's standard dummy text ever since the 1500s, when an unknown printer took a galley of type and scrambled it to make a type specimen book. It has survived not only five centuries, but also the leap into electronic typesetting, remaining essentially unchanged. It was popularised in the 1960s with the release of Letraset sheets containing Lorem Ipsum passages, and more recently with desktop publishing software like Aldus PageMaker including versions of Lorem Ipsum.</p>
<div class="abs btn" style="left:357px;top:500px;width:57px;height:22px;font-size:8px">Read More</div>
<div class="abs divider" style="left:110px;top:523px;width:580px"></div>

<section class="col">
  <h3 style="left:170px;top:557px">Athlete Brand Building</h3>
  <h3 style="left:393px;top:561px">Lifestyle &amp; Sports Marketing</h3>
  <h3 style="left:618px;top:557px">Product Strategy &amp; Launches</h3>
  <div class="abs frame" style="left:75px;top:583px;width:198px;height:97px"><div role="img" aria-label="Close-up of runners' striped athletic shoes" style="background:linear-gradient(135deg,#2d5c8a,#c9a640 50%,#5b6b7a)"></div></div>
  <div class="abs frame" style="left:297px;top:583px;width:198px;height:97px"><div role="img" aria-label="Line of sprinters leaving the starting blocks" style="background:linear-gradient(180deg,#5c6d80,#c48755 55%,#4a88c4)"></div></div>
  <div class="abs frame" style="left:522px;top:583px;width:199px;height:97px"><div role="img" aria-label="High jumper arching over the bar" style="background:linear-gradient(160deg,#4c5a80,#8b95b8 50%,#3d4a6e)"></div></div>
  <div class="abs vline" style="left:285px;top:568px;height:185px"></div>
  <div class="abs vline" style="left:508px;top:568px;height:185px"></div>
  <p style="left:77px;top:691px">Think 'athlete representatives who spent their careers managing some of the world's biggest brands and sponsoring athletes themselves'. We are individuals who build brands, relationships and lives with their athletes.</p>
  <p style="left:300px;top:691px">Think 'athlete representatives who spent their careers managing some of the world's biggest brands and sponsoring athletes themselves'. We are individuals who build brands, relationships and lives with their athletes.</p>
  <p style="left:525px;top:691px">Think 'athlete representatives who spent their careers managing some of the world's biggest brands and sponsoring athletes themselves'. We are individuals who build brands, relationships and lives with their athletes.</p>
  <div class="abs btn" style="left:164px;top:756px;width:42px;height:16px;font-size:6.5px">Read More</div>
  <div class="abs btn" style="left:389px;top:759px;width:42px;height:16px;font-size:6.5px">Read More</div>
  <div class="abs btn" style="left:606px;top:759px;width:42px;height:16px;font-size:6.5px">Read More</div>
  <div class="abs divider" style="left:85px;top:774px;width:185px"></div>
  <div class="abs divider" style="left:308px;top:777px;width:190px"></div>
  <div class="abs divider" style="left:525px;top:777px;width:190px"></div>
</section>

<section class="abs panel">
  <h4 style="left:21px;top:16px">Testimonials</h4>
  <h4 style="left:364px;top:16px">Key Clients</h4>
  <div class="abs" style="left:349px;top:20px;width:1px;height:160px;background:#ccc"></div>
</section>
<span class="qmark" style="left:79px;top:858px">“</span>
<p class="quote" style="top:868px">Lorem Ipsum is simply dummy text of the printing and typesetting industry. Lorem Ipsum has been the industry's standard dummy text ever since the 1500s, when an unknown printer took a galley of type and scrambled it to make a type specimen book. It has survived not only five centuries, but also the leap into electronic typesetting.....</p>
<span class="qmark" style="left:307px;top:905px">”</span>
<span class="author" style="left:364px;top:909px">Dana Orvell</span>
<span class="qmark" style="left:79px;top:926px">“</span>
<p class="quote" style="top:936px">Lorem Ipsum is simply dummy text of the printing and typesetting industry. Lorem Ipsum has been the industry's standard dummy text ever since the 1500s, when an unknown printer took a galley of type and scrambled it to make a type specimen book. It has survived not only five centuries, but also the leap into electronic typesetting.....</p>
<span class="qmark" style="left:307px;top:977px">”</span>
<span class="author" style="left:365px;top:981px">Dana Orvell</span>

<span class="client" style="left:474px;top:885px"><i></i>Corvane</span>
<span class="client" style="left:546px;top:868px"><i></i>Arcway</span>
<span class="client" style="left:670px;top:866px">Dashline</span>
<span class="client" style="left:613px;top:890px"><i style="border-radius:0"></i>Globia</span>
<span class="client" style="left:478px;top:920px">Velora</span>
<span class="client" style="left:547px;top:924px">Everfit</span>
<span class="client" style="left:658px;top:916px"><i></i>Granton</span>
<span class="client" style="left:615px;top:942px">Tellaro</span>
<span class="client" style="left:482px;top:960px"><i></i>Linkwell</span>
<span class="client" style="left:563px;top:970px"><i></i>Apex</span>
<span class="client" style="left:671px;top:965px">Quorra</span>

<footer class="abs footer"></footer>
<ul class="links">
  <li style="top:1059px"><svg width="10" height="9" viewBox="0 0 10 9"><rect x=".5" y="1.5" width="7" height="7" fill="none" stroke="#e8730f"/><path d="M2 4.5l2 2 5-6" fill="none" stroke="#e8730f" stroke-width="1.5"/></svg>Home Page</li>
  <li style="top:1077px"><svg width="10" height="9" viewBox="0 0 10 9"><rect x=".5" y="1.5" width="7" height="7" fill="none" stroke="#e8730f"/><path d="M2 4.5l2 2 5-6" fill="none" stroke="#e8730f" stroke-width="1.5"/></svg>What We Do</li>
  <li style="top:1094px"><svg width="10" height="9" viewBox="0 0 10 9"><rect x=".5" y="1.5" width="7" height="7" fill="none" stroke="#e8730f"/><path d="M2 4.5l2 2 5-6" fill="none" stroke="#e8730f" stroke-width="1.5"/></svg>Athletes</li>
  <li style="top:1111px"><svg width="10" height="9" viewBox="0 0 10 9"><rect x=".5" y="1.5" width="7" height="7" fill="none" stroke="#e8730f"/><path d="M2 4.5l2 2 5-6" fill="none" stroke="#e8730f" stroke-width="1.5"/></svg>Gallery</li>
  <li style="top:1128px"><svg width="10" height="9" viewBox="0 0 10 9"><rect x=".5" y="1.5" width="7" height="7" fill="none" stroke="#e8730f"/><path d="M2 4.5l2 2 5-6" fill="none" stroke="#e8730f" stroke-width="1.5"/></svg>Contact Us</li>
</ul>
<div class="abs nl-title">Newsletter <b>Sign Up</b></div>
<p class="abs nl-text">Want to keep up to date with all our latest news and information? Enter your email below to be added to our mailing list.</p>
<div class="abs signup"></div>
<div class="abs field">Email Address</div>
<div class="abs go">Sign Up</div>
<div class="abs news-title">News Artical</div>
<div class="abs date" style="top:1083px">10<br>May</div>
<p class="abs news" style="top:1086px">Lorem ipsum dolor sit amet, consectetur adipiscing elit.</p>
<div class="abs date" style="top:1121px">10<br>May</div>
<p class="abs news" style="top:1124px">Lorem ipsum dolor sit amet, consectetur adipiscing elit.</p>

<div class="abs band"></div>
<p class="abs copy">Copyright © 2013 Lumbre &amp; Crest. All Rights Reserved.</p>
<div class="social-foot" aria-label="Social links"><span style="left:612px"></span><span style="left:642px"></span><span style="left:672px"></span><span style="left:703px"></span></div>
</body>
</html>
```